International Sex Coach needs a Book Cover in less than 3 days

I need a cover design for my book coming out next week titled "The Hidden Tides of Longing". The book explores the origins of our cultural ideas about sexuality and taboo and is interwoven with personal memoir.
The reader must feel that they are being pulled into an intimate sexual story, but also a deeper understanding of sex itself. Like they are jumping into bed with me, you might say. I would like the title to take up the majority of the space over an image of 3D, very real bed sheets, but I am open to your ideas. I haven't purchased any images yet, but there are a few below I was drawn to.
In its essence, this book is designed to reeducate the reader about sexuality and open them up to a new paradigm of sexual wellness.
The author name is Marisol Tegg. Page must also include the phrase: a revolutionary new approach to sexuality, relationship and love.
Size 6" x 9" (15.24 x 22.86 cm)
Thanks!

Reason: I need more time to review the designs and give feedback.

Target Market(s)

Sexually active men and women.

Industry/Entity Type

Wellness

Font styles to use
Serif

```html
<!DOCTYPE html>
<html lang="en">
<head>
<meta charset="utf-8">
<title>The Hidden Tides of Longing — Cover Options</title>
<link rel="stylesheet" href="https://fonts.googleapis.com/css2?family=Playfair+Display:wght@400;500&family=Libre+Baskerville&display=swap">
<style>
  :root {
    --page: #ffffff;
    --ocean: #0aa3de;
    --ocean-mid: #3bb6e6;
    --ocean-deep: #0a6d9c;
    --ocean-light: #a9e2f6;
    --satin: #f6f3ec;
    --satin-shade: #ddd7ca;
    --satin-glow: #ffffff;
    --mono-light: #e6e6e6;
    --mono-mid: #b9b9b9;
    --mono-dark: #7c7c7c;
    --title-red: #e8403f;
    --ink: #1c1a19;
    --white: #ffffff;
  }
  * { margin: 0; padding: 0; box-sizing: border-box; }
  html, body { width: 1200px; height: 888px; overflow: hidden; background: var(--page); }
  .spread { position: relative; width: 1200px; height: 888px; }

  .cover { position: absolute; top: 0; width: 592px; height: 888px; overflow: hidden; }
  .cover--ocean { left: 0; }
  .cover--satin { left: 608px; }

  .cover__photo { position: absolute; inset: 0; }
  .cover--ocean .cover__photo {
    background:
      radial-gradient(ellipse 38% 22% at 22% 18%, rgba(169,226,246,.75) 0%, transparent 100%),
      radial-gradient(ellipse 30% 30% at 15% 48%, rgba(169,226,246,.55) 0%, transparent 100%),
      radial-gradient(ellipse 34% 30% at 48% 58%, rgba(150,215,240,.7) 0%, transparent 100%),
      radial-gradient(ellipse 28% 14% at 58% 44%, rgba(10,109,156,.35) 0%, transparent 100%),
      radial-gradient(ellipse 40% 22% at 30% 92%, rgba(169,226,246,.6) 0%, transparent 100%),
      radial-gradient(ellipse 22% 40% at 88% 62%, rgba(10,109,156,.55) 0%, transparent 100%),
      radial-gradient(ellipse 35% 20% at 85% 95%, rgba(10,90,135,.6) 0%, transparent 100%),
      linear-gradient(165deg, var(--ocean) 0%, var(--ocean-mid) 45%, #2aa3d6 75%, var(--ocean-deep) 100%);
  }
  .cover--satin .cover__sheets {
    position: absolute; inset: 0;
    background:
      linear-gradient(122deg, transparent 8%, rgba(205,198,184,.55) 14%, transparent 20%),
      linear-gradient(108deg, transparent 30%, var(--satin-glow) 36%, transparent 42%),
      linear-gradient(60deg, transparent 46%, rgba(214,207,193,.6) 52%, transparent 58%),
      linear-gradient(75deg, transparent 62%, var(--satin-glow) 68%, transparent 74%),
      linear-gradient(140deg, transparent 72%, rgba(210,203,188,.55) 80%, transparent 88%),
      linear-gradient(20deg, transparent 80%, rgba(255,255,255,.8) 86%, transparent 92%),
      linear-gradient(180deg, var(--satin) 0%, var(--satin-shade) 50%, var(--satin) 100%);
  }
  .cover--satin .cover__band {
    position: absolute; left: 0; top: 378px; width: 592px; height: 302px;
    background:
      radial-gradient(ellipse 22% 38% at 34% 30%, #f7f7f7 0%, transparent 100%),
      radial-gradient(ellipse 18% 30% at 42% 78%, #fafafa 0%, transparent 100%),
      radial-gradient(ellipse 14% 45% at 76% 55%, rgba(124,124,124,.55) 0%, transparent 100%),
      radial-gradient(ellipse 16% 40% at 6% 50%, rgba(124,124,124,.5) 0%, transparent 100%),
      radial-gradient(ellipse 20% 30% at 92% 20%, rgba(240,240,240,.8) 0%, transparent 100%),
      linear-gradient(90deg, var(--mono-mid) 0%, var(--mono-light) 30%, var(--mono-light) 60%, var(--mono-mid) 85%, var(--mono-light) 100%);
  }

  .title {
    position: absolute; left: 176px; top: 58px; width: 416px;
    font-family: "Playfair Display", "Times New Roman", serif; font-weight: 500; line-height: 1;
  }
  .cover--satin .title { left: 96px; top: 62px; }
  .title__lead { display: block; font-size: 35px; letter-spacing: -0.5px; }
  .title__middle { display: block; margin: -6px 0 0 114px; font-size: 66px; letter-spacing: -1px; }
  .title__middle small { font-size: 38px; }
  .title__main { display: block; margin: -2px 0 0 2px; font-size: 112px; font-weight: 400; color: var(--title-red); letter-spacing: -2px; }
  .cover--ocean .title__lead, .cover--ocean .title__middle { color: var(--white); }
  .cover--satin .title__lead, .cover--satin .title__middle { color: var(--ink); }

  .tagline {
    position: absolute; top: 302px; left: 276px;
    font-family: "Libre Baskerville", Georgia, serif; font-size: 14.5px; line-height: 1.4;
  }
  .tagline span { display: block; }
  .tagline span + span { padding-left: 54px; }
  .cover--ocean .tagline { color: var(--white); }
  .cover--satin .tagline { color: var(--ink); top: 308px; left: 196px; }

  .author { position: absolute; font-family: "Libre Baskerville", Georgia, serif; }
  .cover--ocean .author { left: 30px; bottom: 20px; font-size: 27px; color: var(--white); }
  .cover--satin .author { right: 24px; bottom: 20px; font-size: 24px; color: var(--title-red); }
</style>
</head>
<body>
<main class="spread">
  <section class="cover cover--ocean">
    <div class="cover__photo" role="img" aria-label="Blue-toned close-up photograph of a blonde woman looking down, hand in her hair"></div>
    <h1 class="title">
      <span class="title__lead">The Hidden</span>
      <span class="title__middle">Tides <small>of</small></span>
      <span class="title__main">Longing</span>
    </h1>
    <p class="tagline"><span>A revolutionary new approach to</span><span>sexuality, relationship and love.</span></p>
    <p class="author">Marisol Tegg</p>
  </section>

  <section class="cover cover--satin">
    <div class="cover__sheets" role="img" aria-label="Photograph of soft, rumpled white satin bed sheets"></div>
    <div class="cover__band" role="img" aria-label="Black-and-white photograph band of a blonde woman looking down on white sheets"></div>
    <h1 class="title">
      <span class="title__lead">The Hidden</span>
      <span class="title__middle">Tides <small>of</small></span>
      <span class="title__main">Longing</span>
    </h1>
    <p class="tagline"><span>A revolutionary new approach to</span><span>sexuality, relationship and love.</span></p>
    <p class="author">Marisol Tegg</p>
  </section>
</main>
</body>
</html>
```